依頼概要
■ 依頼の目的/概要

移動販売車の脇に設置するのぼりになります。

■ デザインへの要望

地元の主要農産物(米)をつかっていることを強くアピールし、地域活性につながるような商品(特産品)にしたいです。
商品名は、『ユメサラクレープ』・・・「ユメサラ」とは、岐阜地方で主に栽培されいてる米の銘柄で、実際美味しいです。
県外での『ユメサラ』の認知度を上げることと『ユメサラの生産者』に知ってもらうことが目的なので、メインワードを強調したシンプルなデザインを希望します。
現段階でのイメージは、筆書体かなと思っています。

添付①のテンプレートを使用して、作成してください。(当方、イラストレーター未所持ですので、実際開けるのか確認できません。開けない場合は、お手数ですが、下記のサイトから、ダウンロードをお願いいたします。)
http://www.kasuriya-web.com/original/download.php

また、添付②のロゴマークも組み込んでください。

■店の情報
ユメサラの米粉クレープとタピオカドリンクを可愛いロデルバスで販売しています。
販売場所は、サービスエリア、イベント会場、店舗の駐車場などです。
メイン客層は、女子高校生・大学生などですが、『ユメサラの生産者』である年配の方々にも興味をもっていただきたいです。

参考資料として、実際の車両の画像(添付③)を載せます。あわせて、ご確認下さい。

★キーワード★
メイン(必須) ユメサラクレープ
サブ(必須)  岐阜(県)〔ぎふ(けん)〕
輪之内(町)〔わのうち(ちょう)〕
ロゴマーク

※キーワードの地名は、漢字でも、ひらがなでも構いません。以前は、『岐阜わのうち』で自作したものを使用していました。

■輪之内町の情報
輪之内町は、岐阜県のこの辺りです。添付④確認

■ のぼりの情報

サイズ:横600×縦1800

■ 納品ファイルの希望

イラストレーター形式

■ 進め方

弊社の希望するイメージに近い提案を1つ(場合によって複数)選択させて頂きます。希望に近づけるために、修正要望を個別にさせて頂くこともあります。コンペ方式のため、修正後に当選されない場合も、どうかご了承ください。

■ その他/注意点

選択させて頂いたデザインの著作権(財産権)等の扱いはBrivora利用規約に従い、弊社に譲渡をお願いします。フォントや画像素材などを利用する場合は上記利用用途に使用できることを確認し、第三者の知的財産権等に注意して下さい。
皆様、たくさんの提案ありがとうございます。
すべてと言っていいほどの提案が、イメージ通りの素晴らしい提案です。
ありがとうございます。

今後の修正依頼は、選定後にさせて頂きたく思います。

まだまだ、いろいろな筆文字やデザインを拝見したいと思っております。
引き続きご提案のほど、お願いいたします。

なお、選定は役場(役所)の人や、友人からもっとも支持があったものを選びたいと思います。
残りわずかではございますが、最後までよろしくお願いいたします。
■ 選んだ理由

もっとも支持を集めた提案に決めさせていただきました。
個人的にも、かわいらしさ、バランスの良さが気に入りました。

■ 提案者全員のお礼・コメント

たくさんの提案をしていただき、本当にありがとうございました。
今後ともよろしくお願いいたします。

```html
<!DOCTYPE html>
<html lang="ja">
<head>
<meta charset="utf-8">
<title>ユメサラクレープ のぼり</title>
<link href="https://fonts.googleapis.com/css2?family=Yuji+Boku&family=Yuji+Syuku&family=Rampart+One&display=swap" rel="stylesheet">
<style>
  :root {
    --paper: #ffffff;
    --tab: #e4e4e4;
    --frame: #d2d2d2;
    --map-yellow: #f6c84c;
    --cone-top: #f8df98;
    --cone-bottom: #fcefc6;
    --ink-red: #8a1f22;
    --brush-orange: #e8542a;
    --slice: #f3ebc2;
    --field-green: #c8d98e;
    --logo-green: #2f7a36;
  }
  html, body { margin: 0; padding: 0; overflow: hidden; background: var(--paper); }
  .canvas { position: relative; width: 1200px; height: 3252px; background: var(--paper); overflow: hidden; }
  .tab { position: absolute; background: var(--tab); }
  .banner { position: absolute; left: 140px; top: 140px; width: 920px; height: 3060px; border: 3px solid var(--frame); box-sizing: border-box; background: var(--paper); overflow: hidden; }
  .art { position: absolute; left: 0; top: 0; }

  .origin { position: absolute; margin: 0; font-family: "Yuji Syuku", serif; font-weight: 400; color: var(--ink-red); line-height: 1; white-space: nowrap; -webkit-text-stroke: 3px var(--ink-red); }
  .origin--pref { left: 160px; top: 140px; font-size: 90px; }
  .origin--town { left: 170px; top: 270px; font-size: 150px; letter-spacing: -4px; }
  .origin--born { left: 420px; top: 470px; font-size: 100px; }

  .product { position: absolute; margin: 0; font-family: "Yuji Boku", serif; font-weight: 400; color: var(--brush-orange); writing-mode: vertical-rl; line-height: 1; white-space: nowrap; -webkit-text-stroke: 12px var(--brush-orange); }
  .product--brand { left: 610px; top: 640px; font-size: 290px; letter-spacing: -10px; }
  .product--crepe { left: 230px; top: 1440px; font-size: 300px; letter-spacing: -20px; }

  .slice-text { position: absolute; left: 150px; top: 1040px; font-family: "Yuji Boku", serif; color: var(--brush-orange); font-size: 64px; line-height: 1.15; transform: rotate(-12deg); -webkit-text-stroke: 3px var(--brush-orange); }

  .shop { position: absolute; left: 0; right: 0; top: 2740px; text-align: center; font-family: "Yuji Syuku", serif; }
  .shop__name { display: inline-flex; align-items: center; gap: 26px; font-size: 150px; color: var(--logo-green); line-height: 1; }
  .shop__dot { width: 54px; height: 54px; border-radius: 50%; background: var(--logo-green); }
  .shop__menu { display: flex; justify-content: space-between; align-items: baseline; margin: 40px 50px 0; font-size: 48px; color: var(--ink-red); letter-spacing: 4px; }
</style>
</head>
<body>
<div class="canvas">
  <div class="tab" style="left:275px;top:40px;width:110px;height:90px"></div>
  <div class="tab" style="left:820px;top:40px;width:110px;height:90px"></div>
  <div class="tab" style="left:20px;top:140px;width:110px;height:50px"></div>
  <div class="tab" style="left:20px;top:900px;width:110px;height:50px"></div>
  <div class="tab" style="left:20px;top:1660px;width:110px;height:50px"></div>
  <div class="tab" style="left:20px;top:2420px;width:110px;height:50px"></div>
  <div class="tab" style="left:20px;top:3140px;width:110px;height:50px"></div>

  <section class="banner">
    <svg class="art" width="920" height="3060" viewBox="0 0 920 3060">
      <defs>
        <linearGradient id="coneGrad" x1="0" y1="0" x2="0" y2="1">
          <stop offset="0" stop-color="var(--cone-top)"/>
          <stop offset="1" stop-color="var(--cone-bottom)"/>
        </linearGradient>
      </defs>
      <rect role="img" aria-label="岐阜県の地図のイラスト(黄色)" fill="var(--map-yellow)"
        x="0" y="20" width="880" height="760" rx="90"/>
      <path role="img" aria-label="クレープ生地のイラスト" fill="url(#coneGrad)"
        d="M240 700 L920 560 L920 1000 L520 2740 L420 2740 Z"/>
      <rect role="img" aria-label="クレープの一切れのイラスト" fill="var(--slice)"
        x="80" y="960" width="270" height="340" rx="10" transform="rotate(-10 215 1130)"/>
      <rect role="img" aria-label="輪之内町の地図と稲穂のイラスト" fill="var(--field-green)"
        x="420" y="1700" width="500" height="960" rx="110"/>
    </svg>

    <h2 class="origin origin--pref">岐阜</h2>
    <h2 class="origin origin--town">輪之内町</h2>
    <p class="origin origin--born">生まれの</p>

    <div class="slice-text">&nbsp;フワ<br>フワ</div>

    <h1 class="product product--brand">ユメサラ</h1>
    <p class="product product--crepe">クレープ</p>

    <div class="shop">
      <div class="shop__name"><span class="shop__dot"></span>Ciela</div>
      <div class="shop__menu"><span>crepe</span><span>クレープ・タピオカ シエラ</span><span>tapioca</span></div>
    </div>
  </section>
</div>
</body>
</html>
```